Business Cards

Need business card design that I can update for new employees and details. Needs to incorporate our logo, be bright and fun (in line with tourism and holidays)
Would like a Map of Western Australia on the front with locations all the caravan parks we own (just purchased Tom Price so please include that as well as others listed on our website).
Target Market(s)
Famillies
Contact Information for Business Card
5 Cards -
Mark Pettigrew (Director) e: pettigrew@bluewattle.com.au p: 0462 318 904
Lucy Pettigrew (Director) e: pettigrew@bluewattle.com.au p: 0455 896 320
Peter Halvorsen (General Manager) e: halvorsen@bluewattle.com.au p: 0471 552 648
Mina Halvorsen (General Manager) e: halvorsen@bluewattle.com.au p: 0471 552 649
Neil Whitcombe (Training and Operations Manager) - e: whitcombe@bluewattle.com.au p:0427 160 493
Colors
Designer to choose colors to be used in the design.
Look and feel
Each slider illustrates characteristics of the customer's brand and the style your logo design should communicate.

```html
<!DOCTYPE html>
<html lang="en">
<head>
<meta charset="utf-8">
<title>Bluewattle Tourist Parks – Business Card</title>
<link rel="stylesheet" href="https://fonts.googleapis.com/css2?family=Lora:wght@400;500&display=swap">
<style>
  :root {
    --page-bg: #e8e8e8;
    --teal-top: #3ab7c8;
    --teal-bottom: #5db4a2;
    --teal-ink: #3aa9b4;
    --card-white: #f7f7f7;
    --map-tint: #ececec;
    --ink-dark: #3a3a3a;
    --ink-soft: #6a6a6a;
    --white: #ffffff;
  }
  * { box-sizing: border-box; margin: 0; padding: 0; }
  html, body {
    width: 1200px; height: 726px; overflow: hidden;
    background: var(--page-bg);
    font-family: "Lora", Georgia, serif;
  }
  .sheet { position: relative; width: 1200px; height: 726px; }
  .card {
    position: absolute; top: 198px; width: 540px; height: 330px;
    border-radius: 3px; overflow: hidden;
    box-shadow: 0 6px 18px rgba(0,0,0,0.12);
  }

  /* Front */
  .card--front {
    left: 40px;
    background: linear-gradient(170deg, var(--teal-top) 0%, var(--teal-bottom) 100%);
    color: var(--white);
    text-align: center;
  }
  .brand {
    position: absolute; top: 52px; left: 0; right: 0;
    display: flex; flex-direction: column; align-items: center;
  }
  .brand__square {
    width: 70px; height: 62px; border: 3px solid var(--white);
    margin-bottom: 16px;
  }
  .brand__name {
    font-size: 30px; font-weight: 400; letter-spacing: 3px;
    color: var(--white); line-height: 1.2;
  }
  .locations {
    position: absolute; top: 222px; left: 0; right: 0;
    font-size: 15px; line-height: 1.45; letter-spacing: 0.4px;
  }

  /* Back */
  .card--back { left: 620px; background: var(--card-white); }
  .wa-map {
    position: absolute; top: 0; right: 0; width: 190px; height: 330px;
    background: linear-gradient(180deg, var(--map-tint) 0%, #f1f1f1 100%);
    clip-path: polygon(20% 0, 100% 0, 100% 100%, 55% 100%, 40% 70%, 10% 45%, 25% 25%);
  }
  .back-brand {
    position: absolute; left: 40px; top: 118px;
    display: flex; flex-direction: column; align-items: center; width: 120px;
  }
  .back-brand__square { width: 112px; height: 112px; background: var(--teal-ink); }
  .back-brand__name {
    margin-top: 12px; font-size: 15px; color: var(--teal-ink); letter-spacing: 1px;
  }
  .contact { position: absolute; left: 230px; top: 96px; color: var(--ink-dark); }
  .contact__name { font-size: 24px; font-weight: 500; }
  .contact__role { font-size: 11px; color: var(--ink-soft); margin-top: 2px; }
  .contact__list { list-style: none; margin-top: 24px; }
  .contact__item {
    display: flex; align-items: center; gap: 12px;
    font-size: 14px; line-height: 22px; color: var(--ink-soft);
  }
  .contact__icon { width: 14px; height: 14px; fill: var(--teal-ink); flex: none; }
  .accent { color: var(--teal-ink); }
</style>
</head>
<body>
<main class="sheet">

  <section class="card card--front" aria-label="Card front">
    <div class="brand">
      <div class="brand__square"></div>
      <div class="brand__name">Bluewattle Tourist Parks</div>
    </div>
    <p class="locations">
      Coralbay | Redgum Point | Sandhaven | Pelican Flat | Wattle Creek<br>
      Tidewater | Saltbush Beach House
    </p>
  </section>

  <section class="card card--back" aria-label="Card back">
    <div class="wa-map" role="img" aria-label="Faint outline map of Western Australia"></div>

    <div class="back-brand">
      <div class="back-brand__square"></div>
      <div class="back-brand__name">Bluewattle</div>
    </div>

    <div class="contact">
      <h1 class="contact__name">Peter Halvorsen</h1>
      <p class="contact__role">General Manager</p>
      <ul class="contact__list">
        <li class="contact__item">
          <svg class="contact__icon" viewBox="0 0 16 16" aria-hidden="true"><path d="M3 1h3l1.5 4-2 1.3a9 9 0 0 0 4.2 4.2L11 8.5l4 1.5v3a2 2 0 0 1-2 2A12 12 0 0 1 1 3a2 2 0 0 1 2-2z"/></svg>
          <span class="contact__text">0471 552 648</span>
        </li>
        <li class="contact__item">
          <svg class="contact__icon" viewBox="0 0 16 16" aria-hidden="true"><path d="M1 3h14v1.2L8 9.5 1 4.2z"/><path d="M1 5.5l7 5.3 7-5.3V13H1z"/></svg>
          <span class="contact__text">www.<span class="accent">bluewattle</span>.com.au</span>
        </li>
        <li class="contact__item">
          <svg class="contact__icon" viewBox="0 0 16 16" aria-hidden="true"><circle cx="8" cy="8" r="6.5" fill="none" stroke="#3aa9b4" stroke-width="1.4"/><path d="M1.5 8h13M8 1.5c-3 3.5-3 9.5 0 13M8 1.5c3 3.5 3 9.5 0 13" fill="none" stroke="#3aa9b4" stroke-width="1.2"/></svg>
          <span class="contact__text">halvorsen@bluewattle.com.au</span>
        </li>
      </ul>
    </div>
  </section>

</main>
</body>
</html>
```